Waterjet Cutting Business requires an up to date website

We currently have a website which is outdated and in need of modernization.
We are only looking for a simple website with around 4 pages: Home, Contact Us, Materials, Gallery.
We have some pictures and a logo which can be used.
Our primary business is profile cutting of materials to customers specifications using high-pressure water with abrasive.
We are looking for creative ideas and are open to suggestions!
http://brimfieldcutworks.com/index.asp?pid=1
Update:
Cut quality picture (uploaded)
Map
Comparison to other profile cutting methods such as plasma/laser
Single page style without continuous scrolling
"We can cut virtually any material from any drawing whether it be a Full 3D cad models to hand sketched "
Target Market(s)
Film Industry, Prototype, Engineering, Architect, Artisits, one off designs
Industry/Entity Type
Engineering
Number of Pages Required
1 page
Font styles to use
Look and feel

```html
<!DOCTYPE html>
<html lang="en">
<head>
<meta charset="utf-8">
<title>Brimfield Cutworks – Waterjet Cutting Service</title>
<link rel="stylesheet" href="https://fonts.googleapis.com/css2?family=Open+Sans:ital,wght@0,400;0,600;0,700;1,700&display=swap">
<style>
:root{
  --backdrop:#f7901e;
  --page:#ffffff;
  --ink:#4a4a4a;
  --brand-blue:#1d5aa8;
  --footer:#0b1538;
  --hero-deep:#140f45;
  --hero-mid:#2d3fa6;
  --hero-glow:#6f7be0;
  --white:#ffffff;
}
*{margin:0;padding:0;box-sizing:border-box}
html,body{width:1200px;height:702px;overflow:hidden}
body{background:var(--backdrop);font-family:"Open Sans",Arial,sans-serif;position:relative}
.site{position:absolute;left:62px;top:0;width:1084px;height:702px;background:var(--page);overflow:hidden}
.hero{position:absolute;left:0;top:0;width:1084px;height:350px;
  background:radial-gradient(ellipse at 75% 30%,#a04a8a 0%,transparent 35%),
             linear-gradient(160deg,var(--hero-mid) 0%,var(--hero-deep) 55%,#2a3590 100%)}
.masthead{position:absolute;left:0;top:0;width:1084px;height:60px}
.brand{position:absolute;left:22px;top:16px;display:flex;align-items:center;gap:8px;color:var(--white);font-weight:700;font-size:20px;letter-spacing:.5px}
.brand-mark{width:14px;height:14px;background:var(--white)}
.nav{position:absolute;left:354px;top:20px;display:flex;gap:44px;list-style:none}
.nav a{color:var(--white);text-decoration:none;font-weight:700;font-size:15px}
.phone{position:absolute;right:32px;top:22px;display:flex;align-items:center;gap:6px;color:var(--white);font-weight:700;font-size:14px}
.hero-kicker{position:absolute;left:42px;top:144px;color:var(--white);font-size:19px}
.hero-title{position:absolute;left:42px;top:174px;width:900px;color:var(--white);font-weight:700;font-size:38px;line-height:49px}
.section-head{position:absolute;color:var(--brand-blue);font-weight:700;font-size:16px;letter-spacing:.3px;padding-bottom:2px;border-bottom:1px solid var(--brand-blue)}
.about-head{left:39px;top:359px;width:296px}
.gallery-head{left:634px;top:359px;width:296px}
.about-photo{position:absolute;left:39px;top:393px;width:159px;height:261px;
  background:linear-gradient(180deg,#061a18 0%,#0b2e2a 55%,#1c8c7a 100%)}
.about-text{position:absolute;left:217px;top:414px;width:383px;color:var(--ink);font-size:10.3px;line-height:17.5px;letter-spacing:.1px}
.quality-label{position:absolute;left:230px;top:593px;color:var(--brand-blue);font-weight:700;font-size:12px;line-height:14px;text-align:center}
.quality-scale{position:absolute;left:298px;top:576px;display:flex;gap:1px}
.quality-step{width:58px;text-align:center}
.quality-sample{position:relative;height:59px;background:linear-gradient(90deg,#8d8d8d,#c9c9c9 50%,#9a9a9a)}
.quality-sample span{position:absolute;top:2px;left:0;right:0;color:var(--white);font-size:16px;opacity:.85}
.quality-caption{font-size:5px;line-height:6px;color:#222;margin-top:2px}
.quality-caption em{display:block;font-style:normal;color:#1a2bd0}
.gallery-grid{position:absolute;left:634px;top:397px;display:grid;grid-template-columns:repeat(4,95px);grid-auto-rows:120px;column-gap:15px;row-gap:8px}
.gallery-grid div{width:95px;height:120px}
.footer{position:absolute;left:0;top:679px;width:1084px;height:23px;background:var(--footer);color:var(--white);font-style:italic;font-weight:700;font-size:10px;text-align:center;line-height:23px}
</style>
</head>
<body>
<main class="site">
  <header class="hero" role="img" aria-label="Close-up photograph of a waterjet cutting head over a slatted cutting bed, lit in blue and magenta">
    <div class="masthead">
      <div class="brand"><span class="brand-mark"></span>BRIMFIELD CUTWORKS</div>
      <ul class="nav">
        <li><a href="#">Home</a></li>
        <li><a href="#">Materials</a></li>
        <li><a href="#">Gallery</a></li>
        <li><a href="#">Contact Us</a></li>
      </ul>
      <div class="phone">
        <svg width="13" height="13" viewBox="0 0 24 24" aria-hidden="true"><path fill="#fff" d="M6.6 10.8a15.1 15.1 0 0 0 6.6 6.6l2.2-2.2a1 1 0 0 1 1-.25 11.4 11.4 0 0 0 3.6.57 1 1 0 0 1 1 1V20a1 1 0 0 1-1 1A17 17 0 0 1 3 4a1 1 0 0 1 1-1h3.5a1 1 0 0 1 1 1 11.4 11.4 0 0 0 .57 3.6 1 1 0 0 1-.25 1z"/></svg>
        01632 960418
      </div>
    </div>
    <p class="hero-kicker">Waterjet Cutting Service</p>
    <h1 class="hero-title">We can cut virtually any material from any drawing whether it be a Full 3D cad models to hand sketched "</h1>
  </header>

  <h2 class="section-head about-head">ABOUT</h2>
  <div class="about-photo" role="img" aria-label="Photograph of twin waterjet nozzles cutting over a teal-lit grid bed"></div>
  <p class="about-text">Brimfield Cutworks is part of the Kelsall Arts Group who have been providing a model making and profile cutting service primarily to the film industry for over 10 years. We are used to working within tight timeframes with a fast turnaround for all aspects of Water Jet Profiling, Tile Water Jet Cutting, Abrasive Steel Cutting and Foam Water Jet Cutting.<br>By combining our technical expertise with Vantor's latest dynamic head waterjet technology we are able to offer a Profiling Services which can be tailored to each individual client and completed within fine tolerances to precise specifications.</p>

  <div class="quality-label">CUTTING<br>QUALITY</div>
  <div class="quality-scale">
    <div class="quality-step"><div class="quality-sample" role="img" aria-label="Cut edge sample, quality 1"><span>Q1</span></div><p class="quality-caption">Separation Cut</p></div>
    <div class="quality-step"><div class="quality-sample" role="img" aria-label="Cut edge sample, quality 2"><span>Q2</span></div><p class="quality-caption">Through Cut</p></div>
    <div class="quality-step"><div class="quality-sample" role="img" aria-label="Cut edge sample, quality 3"><span>Q3</span></div><p class="quality-caption">Clean Cut<em>Typicaly closer than +/- 0.010"</em></p></div>
    <div class="quality-step"><div class="quality-sample" role="img" aria-label="Cut edge sample, quality 4"><span>Q4</span></div><p class="quality-caption">Good Edge Finish</p></div>
    <div class="quality-step"><div class="quality-sample" role="img" aria-label="Cut edge sample, quality 5"><span>Q5</span></div><p class="quality-caption">Excellent Edge Finish<em>Typicaly closer than +/- 0.005"</em></p></div>
  </div>

  <h2 class="section-head gallery-head">GALLERY</h2>
  <div class="gallery-grid">
    <div role="img" aria-label="Cutting head throwing sparks on metal" style="background:linear-gradient(180deg,#8a8a8a,#d8d2cc)"></div>
    <div role="img" aria-label="Waterjet head over perforated sheet" style="background:linear-gradient(180deg,#2a2a30,#9aa0a8)"></div>
    <div role="img" aria-label="Nozzle cutting with golden light" style="background:linear-gradient(180deg,#1a1208,#a0702a)"></div>
    <div role="img" aria-label="Nozzle over teal grid bed" style="background:linear-gradient(180deg,#06201c,#2a9c88)"></div>
    <div role="img" aria-label="Cutting head in magenta light" style="background:linear-gradient(180deg,#4a1040,#e048b8)"></div>
    <div role="img" aria-label="Cutting head in blue light" style="background:linear-gradient(180deg,#0c2460,#3a78d0)"></div>
    <div role="img" aria-label="Waterjet machine with hoses" style="background:linear-gradient(180deg,#1a2a40,#6a7c90)"></div>
    <div role="img" aria-label="Cutting head in green light" style="background:linear-gradient(180deg,#082810,#2ab04a)"></div>
  </div>

  <footer class="footer">© Copyright&nbsp; 2018&nbsp; Brimfield Cutworks&nbsp; All rights reserved.</footer>
</main>
</body>
</html>
```